Brochure Design Project

Looking to have a 3 panel (folded) brochure designed for our business.

take inspiration/colorschemes from our upcoming site: www.brightvale.ca/demo

photos and ideas from: www.facebook.com/brightvalecanada
Updates

Lots of new photos uploaded this morning!

New Fonts added to match with our branding. Please use for all main text/headings.

New photo uploaded called 'small'

Please incorporate it into design.

Target Market(s)

Wealthy Home Owners

Industry/Entity Type

Business

Requirements
Must have
• 3 inside panels detail : Home Automation Services (2 of 3 panels) and Home Theater Services (1 of 3 panels).

```html
<!DOCTYPE html>
<html lang="en">
<head>
<meta charset="utf-8">
<title>Brightvale – Home Automation &amp; Home Theater</title>
<link href="https://fonts.googleapis.com/css2?family=Montserrat:wght@300;400&family=Questrial&display=swap" rel="stylesheet">
<style>
  :root {
    --silver-light: #eef0f2;
    --silver-mid: #c9cdd1;
    --silver-dark: #a9aeb3;
    --ink: #2a2c2e;
    --band: #000000;
    --gold-light: #f3c13a;
    --gold: #d99b12;
    --gold-dark: #a86a05;
    --white: #ffffff;
  }
  * { margin: 0; padding: 0; box-sizing: border-box; }
  html, body { width: 1200px; height: 927px; overflow: hidden; }
  body {
    position: relative;
    background: linear-gradient(180deg, var(--silver-light) 0%, var(--silver-mid) 40%, var(--silver-light) 62%, var(--silver-dark) 100%);
    font-family: "Questrial", "Montserrat", sans-serif;
    color: var(--ink);
  }
  .header-band {
    position: absolute; left: 0; top: 37px; width: 1200px; height: 73px;
    background: var(--band);
  }
  .panel-title {
    position: absolute; top: 55px;
    font-family: "Montserrat", sans-serif; font-weight: 300;
    font-size: 37px; letter-spacing: 0.5px; color: var(--white);
    line-height: 1;
  }
  .title-automation { left: 18px; }
  .title-theater { left: 818px; }
  .gold-rule {
    position: absolute; left: 0; top: 110px; width: 1200px; height: 18px;
    background: linear-gradient(180deg, var(--gold-light), var(--gold) 50%, var(--gold-dark));
  }
  .photo { position: absolute; }
  .photo-rack { left: 0; top: 128px; width: 200px; height: 350px;
    background: linear-gradient(90deg, #c9c08a, #1d1f24 15%, #23262c 85%, #d8cf9c); }
  .photo-house { left: 200px; top: 128px; width: 600px; height: 350px;
    background: linear-gradient(180deg, #3d4f7c 0%, #6b7ca6 35%, #b89468 62%, #3d4a2e 100%); }
  .photo-remote { left: 724px; top: 143px; width: 60px; height: 313px; border-radius: 6px;
    background: linear-gradient(90deg, #1a1b1d, #3a3c40 50%, #1a1b1d); }
  .photo-theater { left: 800px; top: 128px; width: 400px; height: 350px;
    background: linear-gradient(180deg, #0a1a3a 0%, #2a2f55 28%, #8a2a1a 55%, #c65a25 72%, #5a1a10 100%); }
  .copy {
    position: absolute; font-size: 17px; line-height: 22px;
  }
  .copy p + p, .copy p + ul { margin-top: 6px; }
  .copy-intro { left: 18px; top: 500px; width: 360px; }
  .copy-scenario { left: 418px; top: 500px; width: 360px; }
  .copy-theater { left: 818px; top: 678px; width: 370px; }
  .feature-list {
    list-style: none; display: grid; grid-template-columns: 160px 200px;
  }
  .copy-theater .feature-list { grid-template-columns: 164px 200px; }
  .feature-list li { position: relative; padding-left: 24px; }
  .feature-list li::before {
    content: ""; position: absolute; left: 3px; top: 9px;
    width: 5px; height: 5px; border-radius: 50%; background: var(--ink);
  }
  .devices { left: 412px; top: 728px; width: 383px; height: 160px; background: none; }
  .device { position: absolute; background: linear-gradient(135deg, #15171a, #3b4048 60%, #15171a); }
  .device-tablet { left: 0; top: 2px; width: 122px; height: 156px; border-radius: 8px; }
  .device-phone { left: 136px; top: 82px; width: 40px; height: 76px; border-radius: 6px; }
  .device-laptop { left: 188px; top: 4px; width: 195px; height: 154px; border-radius: 6px 6px 2px 2px; }
  .rack-frame {
    position: absolute; left: 818px; top: 500px; width: 364px; height: 161px;
    background: linear-gradient(90deg, var(--gold-dark), var(--gold-light) 50%, var(--gold-dark));
  }
  .rack-shot { top: 12px; height: 137px; }
  .rack-shot-1 { left: 12px; width: 100px; background: linear-gradient(180deg, #3b342e, #141518 60%, #6b6c6e); }
  .rack-shot-2 { left: 124px; width: 100px; background: linear-gradient(180deg, #1a2a55, #c8c0a8 50%, #2a2f44); }
  .rack-shot-3 { left: 236px; width: 106px; background: linear-gradient(90deg, #e8e6e2, #1f2430 40%, #1f2430 70%, #f2f1ee); }
</style>
</head>
<body>
  <div class="header-band"></div>
  <h1 class="panel-title title-automation">HOME AUTOMATION</h1>
  <h1 class="panel-title title-theater">HOME THEATER</h1>
  <div class="gold-rule"></div>

  <div class="photo photo-rack" role="img" aria-label="Equipment rack with glowing blue components"></div>
  <div class="photo photo-house" role="img" aria-label="Modern house lit up at dusk"></div>
  <div class="photo photo-remote" role="img" aria-label="Universal remote control"></div>
  <div class="photo photo-theater" role="img" aria-label="Home theater with star ceiling and red seating"></div>

  <div class="copy copy-intro">
    <p>Home Automation is the combination of all of the building’s systems into one easy-to-use interface that is quick to navigate and simple to learn. Whether you are building a multi-million dollar estate, a spec home, or a doing a simple renova-tion, Home Automation technology will enhance any living space.</p>
    <p>Brightvale’s Custom-Designed Home Automation System Can Control:</p>
    <ul class="feature-list">
      <li>Lighting</li><li>Pool/Spa</li>
      <li>Security</li><li>CCTV</li>
      <li>Audio/Video</li><li>Gates/Garage Door</li>
      <li>Climate</li>
    </ul>
  </div>

  <div class="copy copy-scenario">
    <p>Imagine driving up to your home on a rainy Vancouver evening. As you approach, you open up our Smartphone application and press ‘Arrive’. Instantly, the gates and garage door open, the lights turn on, the security system disarms, and the heat in the home rises by 3 degrees. This is no longer science-fiction, this is a Brightvale Home Automation System.</p>
  </div>

  <div class="photo devices" role="img" aria-label="Tablet, smartphone and laptop showing the control app">
    <div class="device device-tablet"></div>
    <div class="device device-phone"></div>
    <div class="device device-laptop"></div>
  </div>

  <div class="rack-frame">
    <div class="photo rack-shot rack-shot-1" role="img" aria-label="Black equipment rack in a room"></div>
    <div class="photo rack-shot rack-shot-2" role="img" aria-label="Open rack with wiring"></div>
    <div class="photo rack-shot rack-shot-3" role="img" aria-label="Rack installed in a closet"></div>
  </div>

  <div class="copy copy-theater">
    <p>We design and install Home Theaters and Media Rooms that amaze! Whether you have a dedicated room or a multi-purpose space, we can engineer a system that truly brings the cinema experience home to you.</p>
    <p>Our Services Include:</p>
    <ul class="feature-list">
      <li>Design</li><li>Soundproofing</li>
      <li>Installation</li><li>Calibration</li>
    </ul>
  </div>
</body>
</html>
```